Engineering firm Hero image for new web page

We are building a new webpage and need a Hero image. I have included a screen grab of the landing page showing where the image will be located. The company tag line (Engineering Tomorrow’s Automation) will be overlaid on the image so we need to be sure it works with the overlay.
We service a number of different industries, and we want something that is not overly specific so that if potential customers see something they don't recognize that we don't run them off. I have found several examples of a style that I think will work very well for us.
I want the Hero image to incorporate our competencies: Engineering, Automation, Integration, Robotics, Controls, Optimization.
There will be a follow on project to create a second image in the same theme which will highlight our industries served. Those will be: Food processing, Oil & Gas, Automotive, Aerospace, Medical, Contract Manufacturing. This image will be just below the hero and will be part of the “who we are section”

```html
<!DOCTYPE html>
<html lang="en">
<head>
<meta charset="utf-8">
<title>Engineering Competencies Hero</title>
<link rel="stylesheet" href="https://fonts.googleapis.com/css2?family=Montserrat:wght@600&display=swap">
<style>
  :root {
    --page-bg: #ffffff;
    --hero-deep: #05101d;
    --hero-mid: #0a2236;
    --hero-glow: #0f3a52;
    --suit: #1a2433;
    --ring: #1fc6dc;
    --ring-soft: rgba(31, 198, 220, 0.45);
    --label: #ffffff;
  }
  html, body {
    margin: 0;
    padding: 0;
    width: 1200px;
    height: 1200px;
    overflow: hidden;
    background: var(--page-bg);
  }
  .canvas {
    position: relative;
    width: 1200px;
    height: 1200px;
  }
  .hero {
    position: absolute;
    left: 94px;
    top: 441px;
    width: 1015px;
    height: 317px;
    overflow: hidden;
    background:
      radial-gradient(ellipse 40% 70% at 20% 50%, var(--hero-glow) 0%, transparent 70%),
      radial-gradient(ellipse 35% 60% at 95% 40%, var(--hero-glow) 0%, transparent 70%),
      linear-gradient(90deg, var(--hero-mid) 0%, var(--hero-deep) 45%, var(--hero-deep) 70%, var(--hero-mid) 100%);
  }
  .hero-photo {
    position: absolute;
    left: 390px;
    top: 0;
    width: 450px;
    height: 317px;
    background:
      radial-gradient(ellipse 22% 40% at 55% 30%, rgba(210, 220, 230, 0.35) 0%, transparent 80%),
      radial-gradient(ellipse 60% 80% at 55% 80%, var(--suit) 0%, transparent 75%);
  }
  .competency-rings {
    position: absolute;
    inset: 0;
    width: 1015px;
    height: 317px;
  }
  .ring-outer {
    fill: none;
    stroke: var(--ring);
    stroke-width: 2.5;
    filter: drop-shadow(0 0 5px var(--ring));
  }
  .ring-inner {
    fill: none;
    stroke: var(--ring-soft);
    stroke-width: 1.5;
    stroke-dasharray: 10 6;
  }
  .ring-label {
    font-family: "Montserrat", sans-serif;
    font-weight: 600;
    font-size: 14px;
    letter-spacing: 0.3px;
    fill: var(--label);
    text-anchor: middle;
    dominant-baseline: middle;
  }
</style>
</head>
<body>
<div class="canvas">
  <section class="hero">
    <div class="hero-photo" role="img" aria-label="Photo of a businessman in a dark suit and tie touching a glowing holographic interface, over a dark blue network backdrop"></div>
    <svg class="competency-rings" viewBox="0 0 1015 317" aria-label="Core competencies">
      <g class="competency">
        <circle class="ring-outer" cx="159" cy="87" r="65"/>
        <circle class="ring-inner" cx="159" cy="87" r="56"/>
        <text class="ring-label" x="159" y="88">OPTIMIZATION</text>
      </g>
      <g class="competency">
        <circle class="ring-outer" cx="319" cy="87" r="65"/>
        <circle class="ring-inner" cx="319" cy="87" r="56"/>
        <text class="ring-label" x="319" y="88">CONTROLS</text>
      </g>
      <g class="competency">
        <circle class="ring-outer" cx="239" cy="227" r="65"/>
        <circle class="ring-inner" cx="239" cy="227" r="56"/>
        <text class="ring-label" x="239" y="228">ROBOTICS</text>
      </g>
      <g class="competency">
        <circle class="ring-outer" cx="755" cy="83" r="65"/>
        <circle class="ring-inner" cx="755" cy="83" r="56"/>
        <text class="ring-label" x="755" y="84">AUTOMATION</text>
      </g>
      <g class="competency">
        <circle class="ring-outer" cx="675" cy="223" r="65"/>
        <circle class="ring-inner" cx="675" cy="223" r="56"/>
        <text class="ring-label" x="675" y="224">INTEGRATION</text>
      </g>
      <g class="competency">
        <circle class="ring-outer" cx="835" cy="223" r="65"/>
        <circle class="ring-inner" cx="835" cy="223" r="56"/>
        <text class="ring-label" x="835" y="224">ENGINEERING</text>
      </g>
    </svg>
  </section>
</div>
</body>
</html>
```